Redesign, cleanup and edit my Presentations

I have a series of power points that I use for training purposes. They were made by me over time. During the last couple years, I have evolved their look and content over time, but not consistently. More specifically, I have not gone back to re-edit the older decks. So, some decks are too wordy, too long, or and don't look consistent.

I am looking someone who can create a good design that I can use going forward, and who could also apply that theme to the existing decks, along with editing the existing, and future decks, too.

I have a lot of slides to produce and/or edit -approximately 500. But this request is a test to find a powerpoint partner. I am supplying 2 decks. One that's older and more wordy than the other. I would like to see what you would suggest we do differently. So that's what you are bidding on today. Also, you do not have to complete deck "Phase 7.4." I only need enough of the deck done to see where you would take it. Maybe 10 slides? Your choice. However, with that deck, there are lots of opportunities to clarify, re-align, and minimize within that deck.

But, if you are selected, I want to engage with you on an ongoing basis, and send more material your way. Then, you will be engaged to complete all decks.

Please ask me any questions to help you gain a better understanding of this project.

Target Market(s)

People in management, technical, medical, and financial fields who wish to become independent consultants.

Industry/Entity Type

Business Consultant

Font styles to use
Sans Serif

Requirements
Must have
• Use the existing color theme:
• yellow/gold - #f5b300,
• blue - 2b74a6
• Logo doesn't change
• Preferred fonts: Raleway for headings and Open Sans for general text
• Any pictures and graphics should have no copyright restrictions. That is, I should have use of the work without charge.
Nice to have
• I prefer a flat graphic style, although you can use pictures where it conveys a point more effectively.
• Ability to convert the presentations to Google Slides and Apple's Keynote apps.
• Ability to convert presentation to video
Should not have
• Restricted use graphics, photos, or other content.

```html
<!DOCTYPE html>
<html lang="en">
<head>
<meta charset="utf-8">
<title>Vantora – Step 3.1 Personas</title>
<link href="https://fonts.googleapis.com/css2?family=Raleway:wght@300;400;700;800&family=Open+Sans:wght@400;600&display=swap" rel="stylesheet">
<style>
  :root {
    --gold: #f5b300;
    --gold-soft: #f8cf6a;
    --gold-deep: #d4a53c;
    --blue: #2b74a6;
    --blue-deep: #1f6e9c;
    --red: #c00000;
    --grey: #7f7f7f;
    --white: #ffffff;
  }
  * { margin: 0; padding: 0; box-sizing: border-box; }
  html, body { width: 1200px; height: 1080px; overflow: hidden; background: var(--white); }
  .stage {
    position: absolute; left: 0; top: 0;
    width: 2000px; height: 1800px;
    transform: scale(0.6); transform-origin: 0 0;
  }
  .slide { position: absolute; left: 200px; width: 1600px; height: 900px; overflow: hidden; background: var(--white); }
  .slide--title { top: 0; border-left: 1px solid #eee; border-right: 1px solid #eee; }
  .slide--journey { top: 900px; border-top: 1px solid #bfbfbf; border-left: 1px solid #eee; border-right: 1px solid #eee; }

  .brand { position: absolute; left: 128px; top: 212px; display: flex; align-items: center; gap: 16px; }
  .brand__dot { width: 64px; height: 64px; border-radius: 50%; background: var(--gold); }
  .brand__name { font-family: "Open Sans", sans-serif; font-weight: 600; font-size: 78px; color: var(--blue); letter-spacing: 1px; }

  .title-step { position: absolute; left: 138px; top: 408px; font-family: "Raleway", sans-serif; font-weight: 800; font-size: 122px; color: var(--blue); letter-spacing: -1px; }
  .title-topic { position: absolute; left: 140px; top: 572px; font-family: "Raleway", sans-serif; font-weight: 300; font-size: 66px; color: var(--gold); letter-spacing: 2px; }

  .skyline-wash {
    position: absolute; left: 0; top: 330px; width: 1000px; height: 420px;
    background: linear-gradient(180deg, rgba(236,238,242,0) 0%, rgba(236,238,242,0.55) 50%, rgba(255,255,255,0) 100%);
  }
  .hero-photo {
    position: absolute; left: 980px; top: 0; width: 620px; height: 900px;
    background: linear-gradient(180deg, var(--gold-soft) 0%, #eec46a 40%, var(--gold-deep) 70%, #f1dca8 90%, rgba(255,255,255,0.9) 100%);
  }

  .journey-title { position: absolute; left: 82px; top: 82px; font-family: "Raleway", sans-serif; font-weight: 800; font-size: 72px; color: var(--blue); letter-spacing: -1px; }
  .journey-map { position: absolute; left: -200px; top: -900px; width: 2000px; height: 1800px; }
  .stage-label { font-family: "Raleway", sans-serif; font-weight: 700; font-size: 31px; fill: var(--blue); }
  .callout-text { font-family: "Open Sans", sans-serif; font-size: 28px; fill: var(--white); }
  .note-text { font-family: "Open Sans", sans-serif; font-size: 28px; fill: var(--white); }
  .trigger-title { font-family: "Open Sans", sans-serif; font-weight: 600; font-size: 32px; fill: var(--blue); }
  .trigger-item { font-family: "Open Sans", sans-serif; font-size: 22px; fill: var(--grey); }

  .footer-band { position: absolute; left: 0; bottom: 0; width: 1600px; height: 48px; background: var(--blue); }
  .footer-corner { position: absolute; right: 0; bottom: 0; width: 0; height: 0; border-left: 46px solid transparent; border-bottom: 46px solid var(--gold); }
  .footer-badge { position: absolute; left: 32px; bottom: 10px; width: 78px; height: 78px; border-radius: 50%; background: var(--white); display: flex; align-items: center; justify-content: center; }
  .footer-badge__dot { width: 36px; height: 36px; border-radius: 50%; background: var(--gold); }
  .footer-credit { position: absolute; right: 64px; bottom: 12px; font-family: "Open Sans", sans-serif; font-size: 19px; color: var(--white); }
  .footer-credit b { margin-left: 24px; font-weight: 600; }
  .footer-credit span { margin-left: 22px; }
</style>
</head>
<body>
<div class="stage">

  <section class="slide slide--title">
    <div class="skyline-wash" role="img" aria-label="Faded city skyline seen through office windows"></div>
    <div class="hero-photo" role="img" aria-label="Photo of a businessman standing at a window overlooking a city skyline, in warm gold tones"></div>
    <div class="brand"><span class="brand__dot"></span><span class="brand__name">Vantora</span></div>
    <h1 class="title-step">Step 3.1</h1>
    <p class="title-topic">PERSONAS</p>
  </section>

  <section class="slide slide--journey">
    <h2 class="journey-title">CUSTOMER JOURNEY Map</h2>

    <svg class="journey-map" viewBox="0 0 2000 1800" aria-label="Customer journey loop diagram">
      <g fill="none" stroke="var(--blue-deep)" stroke-width="28" stroke-linecap="round">
        <path d="M523 1510 C500 1400 560 1335 655 1305 C750 1265 850 1245 945 1232 C1150 1200 1380 1210 1515 1265 C1640 1320 1625 1430 1560 1485 C1450 1590 1220 1625 1030 1632"/>
        <path d="M523 1510 C560 1420 750 1350 950 1345 C1150 1340 1225 1400 1205 1455 C1180 1530 1060 1565 950 1592"/>
        <path d="M523 1510 C560 1570 620 1592 710 1605 L840 1610"/>
      </g>
      <polygon points="985,1635 1045,1598 1035,1632 1045,1662" fill="var(--blue-deep)"/>
      <polygon points="900,1603 955,1562 948,1596 965,1625" fill="var(--blue-deep)"/>

      <g stroke="var(--white)" stroke-width="5" fill="var(--gold)">
        <circle cx="654" cy="1309" r="32"/>
        <circle cx="946" cy="1232" r="32"/>
        <circle cx="1516" cy="1265" r="32"/>
        <circle cx="596" cy="1577" r="32"/>
        <circle cx="710" cy="1607" r="32"/>
        <circle cx="842" cy="1610" r="50"/>
        <circle cx="523" cy="1510" r="32" fill="var(--red)"/>
      </g>

      <path d="M547 1100 H716 Q730 1100 730 1114 V1192 Q730 1206 716 1206 H700 L715 1245 L648 1206 H547 Q533 1206 533 1192 V1114 Q533 1100 547 1100 Z" fill="var(--gold)"/>
      <text class="callout-text" x="632" y="1163" text-anchor="middle">Information</text>

      <path d="M1219 1076 H1388 Q1402 1076 1402 1090 V1094 L1425 1106 L1402 1118 V1168 Q1402 1182 1388 1182 H1219 Q1205 1182 1205 1168 V1090 Q1205 1076 1219 1076 Z" fill="var(--gold)"/>
      <text class="callout-text" x="1302" y="1139" text-anchor="middle">Education</text>

      <path d="M1452 1050 H1734 Q1754 1050 1754 1070 V1175 Q1754 1195 1734 1195 H1548 L1518 1222 L1488 1195 H1452 Q1432 1195 1432 1175 V1070 Q1432 1050 1452 1050 Z" fill="var(--blue-deep)"/>
      <text class="note-text" x="1452" y="1101">The first opportunity</text>
      <text class="note-text" x="1452" y="1131">to talk to someone in</text>
      <text class="note-text" x="1452" y="1161">person is likely here!</text>

      <path d="M691 1418 H912 Q926 1418 926 1432 V1511 Q926 1525 912 1525 H885 L850 1546 L820 1525 H691 Q677 1525 677 1511 V1432 Q677 1418 691 1418 Z" fill="var(--gold)"/>
      <text class="callout-text" x="801" y="1482" text-anchor="middle">Transformation</text>

      <text class="stage-label" x="610" y="1310" text-anchor="end">Awareness</text>
      <text class="stage-label" x="798" y="1202">Consider</text>
      <text class="stage-label" x="1567" y="1240">Evaluate</text>
      <text class="stage-label" x="498" y="1643">Advocate</text>
      <text class="stage-label" x="672" y="1678">Enjoy</text>
      <text class="stage-label" x="830" y="1702">BUY!</text>

      <text class="trigger-title" x="267" y="1514">Trigger Event</text>
      <text class="trigger-item" x="267" y="1540">•&#160;&#160;&#160;Emotional event</text>
      <text class="trigger-item" x="267" y="1564">•&#160;&#160;&#160;Economic event</text>
      <text class="trigger-item" x="267" y="1588">•&#160;&#160;&#160;Regulatory event</text>
    </svg>

    <div class="footer-band"></div>
    <div class="footer-corner"></div>
    <div class="footer-badge"><span class="footer-badge__dot"></span></div>
    <p class="footer-credit">Vantora LLC<span>|</span><b>2</b></p>
  </section>

</div>
</body>
</html>
```